business card with logo Velmora Nails & Spa 2816 SW Quillan Ave Portland OR 97384

Would like to have a business card with our logo.
like bottle of polish with our logo or letter V on it
want something that first glance would let you know that it is a nail salon.
like the hands with polish bottle dripping.
like black or White back ground

Velmora Nails & Spa
(The Velvet Retreat)
2816 SW Quillan Ave
Portland, OR 97384
Call or Text: 1-503-555-0148
www.VelmoraNailsnSpa.example
Open 7 days a week.
After 7:00 PM is by appointment only.
Closed only on Thanksgiving & Christmas.

Target Market(s)

20%Man and 80%Woman 13-70

Industry/Entity Type

Business

Contact Information for Business Card

Elegant with Logo-Business name- address-phone-open days. closed day.

Font styles to use
Decorative
Script

Colors
000000

Requirements
Must have
• Logo and place for Technician Name
• Velmora Nails & Spa
• (The Velvet Retreat)
• 2816 SW Quillan Ave
• Portland, OR 97384
• Call or Text: 1-503-555-0148
• Open 7 days a week
• Closed only on Thanksgiving & Christmas.
• We accepted all major credit cards but prefer cash. Thank you
Nice to have
• Nail polish bottle with our Logo or letter V
Should not have
• too colorful

```html
<!DOCTYPE html>
<html lang="en">
<head>
<meta charset="utf-8">
<title>Velmora Nails &amp; Spa – Business Card</title>
<link rel="stylesheet" href="https://fonts.googleapis.com/css2?family=Lato:ital,wght@0,300;0,400;0,700;1,300&display=swap">
<style>
  :root{
    --stage:#e9e6e2;
    --ink:#111111;
    --black:#0b0b0b;
    --white:#ffffff;
    --red:#e02a2f;
    --lime:#a9cf3a;
    --muted:#cfcfcf;
    --polish:#e0457b;
    --skin:#f1c3b0;
  }
  *{box-sizing:border-box;margin:0;padding:0}
  html,body{width:1200px;height:950px;overflow:hidden}
  body{background:var(--stage);font-family:"Lato",sans-serif;position:relative}

  .card{position:absolute;left:250px;width:700px;height:400px;overflow:hidden;
        box-shadow:0 10px 28px rgba(0,0,0,.28)}
  .card--front{top:50px;background:var(--white)}
  .card--back{top:500px;background:radial-gradient(ellipse at 70% 40%,#3a3a3a 0%,#141414 55%,#050505 100%)}

  .front-shapes{position:absolute;inset:0}

  .brand{position:absolute;left:48px;top:150px;display:flex;align-items:center;gap:14px;
         color:var(--ink);font-weight:400;font-size:30px;line-height:1.15;letter-spacing:.5px}
  .brand__dot{width:14px;height:14px;border-radius:50%;background:var(--red);flex:none}
  .brand__name{display:flex;flex-direction:column}

  .contact{position:absolute;right:44px;top:48px;text-align:right;color:var(--white);
           font-weight:300;font-size:17px;line-height:1.55}
  .contact__name{color:var(--red);font-weight:400;font-size:25px;line-height:1.2}
  .contact__role{margin-bottom:18px}
  .contact__line{display:flex;justify-content:flex-end;align-items:center;gap:10px}
  .contact__line svg{width:16px;height:16px;fill:var(--red)}
  .tagline{position:absolute;right:44px;bottom:26px;color:var(--white);font-weight:300;font-size:15px}

  .hours{position:absolute;left:42px;top:70px;color:var(--white);font-weight:300;font-size:22px;line-height:1.35}
  .hours__note{font-style:italic;font-size:13px;margin-top:6px;color:var(--muted)}
  .payments{position:absolute;left:42px;top:200px;display:flex;gap:14px}
  .payments__item{color:var(--white);font-weight:700;font-size:14px;padding:5px 10px;
                  border:1px solid #555;border-radius:3px}

  .polish-bottle{position:absolute;left:470px;top:30px;width:150px;height:60px;border-radius:10px;
                 background:linear-gradient(90deg,var(--polish),#b22a5c 60%,#777 61%,#ddd)}
  .hands{position:absolute;left:380px;top:260px;width:320px;height:120px;border-radius:60px 0 0 60px;
         background:linear-gradient(180deg,#f6d3c4,var(--skin) 60%,#d99c86)}
</style>
</head>
<body>

<section class="card card--front" aria-label="Business card front">
  <svg class="front-shapes" viewBox="0 0 700 400" aria-hidden="true">
    <path d="M430 0 C330 70 390 300 190 400 L700 400 L700 0 Z" fill="var(--black)"/>
    <path d="M468 0 C420 20 395 50 385 110" fill="none" stroke="var(--lime)" stroke-width="10" stroke-linecap="round"/>
    <path d="M0 392 C110 385 180 360 235 300" fill="none" stroke="var(--red)" stroke-width="9" stroke-linecap="round"/>
  </svg>

  <div class="brand"><span class="brand__dot"></span>
    <div class="brand__name"><span>Velmora</span><span>Nails &amp; Spa</span></div>
  </div>

  <div class="contact">
    <div class="contact__name">Corinne Dalby</div>
    <div class="contact__role">Nail Technician</div>
    <div>2816 SW Quillan Ave</div>
    <div>Portland, OR 97384</div>
    <div class="contact__line">1-503-555-0148
      <svg viewBox="0 0 24 24"><path d="M6.6 10.8a15 15 0 0 0 6.6 6.6l2.2-2.2a1 1 0 0 1 1-.25 11.4 11.4 0 0 0 3.6.6 1 1 0 0 1 1 1V20a1 1 0 0 1-1 1A17 17 0 0 1 3 4a1 1 0 0 1 1-1h3.5a1 1 0 0 1 1 1c0 1.25.2 2.45.6 3.6a1 1 0 0 1-.25 1z"/></svg>
    </div>
    <div class="contact__line">corinne@velmora.example
      <svg viewBox="0 0 24 24"><path d="M3 5h18v14H3z M3 5l9 7 9-7" fill="var(--red)"/><path d="M3 5l9 7 9-7" fill="none" stroke="var(--black)" stroke-width="1.6"/></svg>
    </div>
  </div>

  <div class="tagline">Velmora Nails &amp; Spa The Velvet Retreat</div>
</section>

<section class="card card--back" aria-label="Business card back">
  <div class="polish-bottle" role="img" aria-label="Pink nail polish bottle with letter V on the label"></div>

  <div class="hours">
    <div>Open 7 days a week</div>
    <div>Closed only on Thanksgiving &amp; Christmas.</div>
    <div class="hours__note">We accept all major credit cards but prefer cash. Thank you</div>
  </div>

  <div class="payments">
    <span class="payments__item">Cardline</span>
    <span class="payments__item">Amplex</span>
    <span class="payments__item">Findpay</span>
  </div>

  <div class="hands" role="img" aria-label="Two hands with pink painted nails"></div>
</section>

</body>
</html>
```